Painting Valtoni Renovations New buildings

Paint jobs plasterwork renovations new building customer painter paper drywall Entsorgungen.neukunden win color splash pleasure in colors competent clean fast reliable new try build demolition color combinations color concepts offers washing façade painting wood stains new projects old building renovations yes no beautiful new old sell secure solve paint over paint paint spray paint lye assemble disassemble sell buy trade oil dust new old assembly disassembly putty sanding fashion devastation copying belief feng shui kleopatra pompes beer colors swamp lime abrasion release tighten

Target Market(s)

construction industry

Contact Information for Business Card

Maler

Font styles to use
Serif

Colors
f04a50
959595

Requirements
Must have
• elegant appearance
Nice to have
• simply goal-oriented clientele in detail
Should not have
• too colorful

```html
<!DOCTYPE html>
<html lang="en">
<head>
<meta charset="utf-8">
<title>Lunaro Malerbetrieb – Business Card</title>
<link rel="stylesheet" href="https://fonts.googleapis.com/css2?family=Libre+Baskerville:ital,wght@0,400;0,700;1,400&display=swap">
<style>
  :root {
    --stage: #e4e4e6;
    --card: #ffffff;
    --brand-blue: #1f4a85;
    --accent-red: #f04a50;
    --accent-grey: #959595;
    --ink-white: #ffffff;
    --shadow: rgba(0,0,0,0.18);
  }
  * { margin: 0; padding: 0; box-sizing: border-box; }
  html, body { width: 1200px; height: 800px; overflow: hidden; background: var(--stage); }
  .canvas {
    width: 1200px; height: 800px; position: relative;
    font-family: "Libre Baskerville", "Times New Roman", serif;
  }
  .card {
    position: absolute; left: 290px; width: 620px; height: 354px;
    background: var(--card); border-radius: 22px; overflow: hidden;
    box-shadow: 0 10px 30px var(--shadow);
  }
  .card--front { top: 26px; }
  .card--back { top: 420px; }

  .wordmark { position: absolute; display: flex; flex-direction: column; align-items: flex-start; color: var(--brand-blue); }
  .wordmark__row { display: flex; align-items: center; gap: 12px; }
  .wordmark__dot { width: 22px; height: 22px; border-radius: 50%; background: var(--brand-blue); }
  .wordmark__name { font-size: 56px; font-weight: 700; line-height: 1; letter-spacing: 1px; }
  .wordmark__trade { font-size: 15px; font-weight: 400; margin-top: 6px; margin-left: 34px; letter-spacing: 2px; }
  .card--front .wordmark { left: 50%; top: 50%; transform: translate(-50%, -50%); }
  .card--back .wordmark { left: 56px; top: 104px; }
  .card--back .wordmark__name { font-size: 46px; }

  .card__wave { position: absolute; inset: 0; }

  .holder { position: absolute; right: 34px; top: 28px; text-align: right; color: var(--brand-blue); }
  .holder__name { font-size: 22px; font-weight: 700; }
  .holder__role { font-size: 13px; font-weight: 400; margin-top: 2px; }

  .contact { position: absolute; right: 28px; top: 170px; color: var(--ink-white); font-size: 12.5px; line-height: 1.55; text-align: right; }
  .contact__address { margin-bottom: 14px; }
  .contact__line { display: flex; justify-content: flex-end; align-items: center; gap: 8px; white-space: nowrap; }
  .contact__icon { width: 11px; height: 11px; flex: none; }
</style>
</head>
<body>
<main class="canvas">

  <section class="card card--front" aria-label="Business card front">
    <div class="wordmark">
      <div class="wordmark__row">
        <span class="wordmark__dot"></span>
        <span class="wordmark__name">Lunaro</span>
      </div>
      <span class="wordmark__trade">Malerbetrieb</span>
    </div>
  </section>

  <section class="card card--back" aria-label="Business card back">
    <svg class="card__wave" viewBox="0 0 620 354" width="620" height="354" aria-hidden="true">
      <defs>
        <linearGradient id="accent-sweep" x1="0" y1="1" x2="1" y2="0">
          <stop offset="0" stop-color="#f04a50"/>
          <stop offset="1" stop-color="#959595"/>
        </linearGradient>
      </defs>
      <path class="wave__field" d="M170,354 C290,330 360,260 385,190 C410,120 480,100 620,92 L620,354 Z" fill="var(--brand-blue)"/>
      <path class="wave__swoosh" d="M110,354 C240,325 320,260 350,185 C375,125 430,100 520,88 C450,110 405,140 378,200 C345,275 270,330 150,354 Z" fill="var(--brand-blue)"/>
      <path class="wave__accent" d="M0,334 C150,330 260,285 300,215 C315,185 322,155 325,125 C330,172 320,207 305,237 C260,305 160,338 0,344 Z" fill="url(#accent-sweep)"/>
    </svg>

    <div class="wordmark">
      <div class="wordmark__row">
        <span class="wordmark__dot"></span>
        <span class="wordmark__name">Lunaro</span>
      </div>
      <span class="wordmark__trade">Malerbetrieb</span>
    </div>

    <div class="holder">
      <p class="holder__name">Merenda Valtoni</p>
      <p class="holder__role">Manager</p>
    </div>

    <div class="contact">
      <div class="contact__address">
        <p class="contact__line">PO BOX 47, Harbour Lane</p>
        <p class="contact__line">8 Elm Street Melbourne</p>
      </div>
      <p class="contact__line">(555) 310 4826
        <svg class="contact__icon" viewBox="0 0 12 12" aria-hidden="true"><rect x="1" y="1" width="10" height="10" rx="1.5" fill="none" stroke="#fff" stroke-width="1.4"/></svg>
      </p>
      <p class="contact__line">info@lunaromaler.com
        <svg class="contact__icon" viewBox="0 0 12 12" aria-hidden="true"><rect x="0.5" y="2" width="11" height="8" fill="#fff"/><path d="M0.5,2 L6,7 L11.5,2" fill="none" stroke="#1f4a85" stroke-width="1"/></svg>
      </p>
      <p class="contact__line">www.lunaromaler.com
        <svg class="contact__icon" viewBox="0 0 12 12" aria-hidden="true"><circle cx="6" cy="6" r="5" fill="none" stroke="#fff" stroke-width="1.2"/><path d="M1,6 H11 M6,1 C3,4 3,8 6,11 M6,1 C9,4 9,8 6,11" fill="none" stroke="#fff" stroke-width="0.9"/></svg>
      </p>
    </div>
  </section>

</main>
</body>
</html>
```